LumaVault (Website about Banking Software)

I have a business about banking Software and I need an Avatar and FULL imagen for my friendwall . I have my logo, so I think is easy to create the images that I want . I will buy this design http://www.pagefoundry-example.net/demo/48213.html, so please the avatar & full imagen need to combine with my logo and the website.

Target Market(s)

Banking Software

Industry/Entity Type

Bank

Font styles to use
Serif
Sans Serif

Colors
0255a3
3176b5

Requirements
Must have
• The best Quality for this project. Also you can put this sentence " Who said online banking cannot be beautiful? "
Nice to have
• The avatar and full imagen need to combine with my template http://www.pagefoundry-example.net/demo/48213.html . Please don't forge use the logo colors .
Should not have
• I don't want pigs avatars ,

```html
<!DOCTYPE html>
<html lang="en">
<head>
<meta charset="utf-8">
<title>LumaVault – Cover</title>
<link rel="stylesheet" href="https://fonts.googleapis.com/css2?family=Raleway:wght@500&display=swap">
<style>
  :root {
    --brand-copper: #b8732a;
    --brand-navy: #26387a;
    --ink-black: #111111;
    --caption-band: rgba(118, 138, 170, 0.62);
    --caption-text: #ffffff;
    --photo-light: #eef0f2;
    --photo-mid: #c9cdd2;
    --photo-dark: #4a4643;
  }
  html, body {
    margin: 0;
    padding: 0;
    overflow: hidden;
    background: #ffffff;
  }
  .cover {
    position: relative;
    width: 1200px;
    height: 444px;
    overflow: hidden;
    font-family: "Raleway", sans-serif;
  }
  .cover-photo {
    position: absolute;
    inset: 0;
    background:
      radial-gradient(ellipse at 45% 75%, rgba(90, 95, 110, 0.45) 0%, rgba(90, 95, 110, 0) 45%),
      linear-gradient(90deg, var(--photo-dark) 0%, #8a8580 18%, var(--photo-mid) 38%, var(--photo-light) 70%, #f7f8f9 100%);
  }
  .brand-lockup {
    position: absolute;
    top: 30px;
    left: 600px;
    display: flex;
    align-items: center;
    gap: 22px;
  }
  .brand-mark {
    width: 84px;
    height: 84px;
    border-radius: 14px;
    background: var(--brand-copper);
  }
  .brand-name {
    font-size: 78px;
    font-weight: 500;
    color: var(--brand-navy);
    letter-spacing: -1px;
    line-height: 1;
  }
  .avatar-tile {
    position: absolute;
    left: 39px;
    top: 213px;
    width: 239px;
    height: 240px;
    box-sizing: border-box;
    border: 4px solid var(--ink-black);
    background: var(--brand-copper);
  }
  .avatar-mark {
    position: absolute;
    left: 50%;
    top: 44px;
    width: 90px;
    height: 90px;
    margin-left: -45px;
    border-radius: 50%;
    background: #ffffff;
  }
  .avatar-name {
    position: absolute;
    left: 0;
    right: 0;
    top: 150px;
    text-align: center;
    font-size: 36px;
    font-weight: 500;
    color: var(--brand-navy);
    letter-spacing: -0.5px;
  }
  .tagline-band {
    position: absolute;
    left: 384px;
    top: 289px;
    width: 816px;
    height: 120px;
    background: var(--caption-band);
    display: flex;
    align-items: center;
    justify-content: center;
  }
  .tagline {
    margin: 0;
    text-align: center;
    color: var(--caption-text);
    font-size: 43px;
    font-weight: 500;
    line-height: 1.13;
  }
</style>
</head>
<body>
  <div class="cover">
    <div class="cover-photo" role="img" aria-label="Photo of a person at a desk browsing a banking website on a tablet"></div>

    <div class="brand-lockup">
      <div class="brand-mark"></div>
      <span class="brand-name">LumaVault</span>
    </div>

    <div class="avatar-tile">
      <div class="avatar-mark"></div>
      <div class="avatar-name">LumaVault</div>
    </div>

    <div class="tagline-band">
      <p class="tagline">Who said online banking cannot<br>be beautiful?</p>
    </div>
  </div>
</body>
</html>
```